This book will apply the 12 Steps to gaming addiction, also known as video game addiction. The primary purpose of the book is to provide an effective solution for this new type of addiction. The solution is based on the rich and successful concepts of traditional twelve-step programs like RL.

The title on the cover will be "Nine Doors Past the Glowing Screen" and "by Martin Quorby". A subtitle can be used if it works in your design of "A Practical Path Beyond Compulsive Console Play". Cover will be for a 6" x 9" book approximately 110 pages in length.

Some back cover text including some review quotes and an author bio are in the attached Word doc. There is also an author photo attached for for the back cover.

Requirements
Must have
• For the cover design it could be stylized, or an image, a partial image, or whatever. I am open to suggestions. Think about what would be noticed by a person searching for help with moderating their video game use, or by the parents or loved ones of problem gamers. Something contemporary and eye catching.

```html
<!DOCTYPE html>
<html lang="en">
<head>
<meta charset="utf-8">
<title>Nine Doors Past the Glowing Screen — Martin Quorby</title>
<link rel="stylesheet" href="https://fonts.googleapis.com/css2?family=Anton&family=Montserrat:wght@200;700;900&family=Italianno&display=swap">
<style>
  :root {
    --ink-night: #0f1320;
    --ink-deep: #0b0e18;
    --paper: #ffffff;
    --controller-blue: #4a5a86;
    --glow-red: #e3321a;
    --glow-hot: #ff6a3a;
    --skin-shadow: #5a4440;
  }
  html, body {
    margin: 0;
    padding: 0;
    width: 848px;
    height: 1200px;
    overflow: hidden;
    background: var(--ink-night);
  }
  .cover {
    position: relative;
    width: 848px;
    height: 1200px;
    overflow: hidden;
    background: var(--ink-night);
  }
  .cover-photo {
    position: absolute;
    left: 0;
    top: 540px;
    width: 848px;
    height: 600px;
    background:
      radial-gradient(ellipse 170px 60px at 432px 352px, var(--glow-hot) 0%, var(--glow-red) 40%, rgba(227,50,26,0) 100%),
      radial-gradient(ellipse 300px 150px at 430px 300px, rgba(74,90,134,0.85) 0%, rgba(74,90,134,0.35) 60%, rgba(15,19,32,0) 100%),
      radial-gradient(ellipse 160px 200px at 80px 230px, rgba(90,68,64,0.6) 0%, rgba(15,19,32,0) 100%),
      radial-gradient(ellipse 160px 200px at 770px 230px, rgba(90,68,64,0.55) 0%, rgba(15,19,32,0) 100%),
      linear-gradient(180deg, var(--ink-night) 0%, #1d2233 30%, #1a1f30 70%, var(--ink-deep) 100%);
  }
  .cover-type {
    position: absolute;
    left: 0;
    top: 0;
  }
  .byline {
    font-family: "Montserrat", sans-serif;
    font-weight: 700;
    font-size: 25px;
    fill: var(--paper);
  }
  .title-script {
    font-family: "Italianno", cursive;
    font-size: 68px;
    fill: var(--paper);
  }
  .title-block {
    font-family: "Anton", sans-serif;
    font-size: 160px;
    fill: var(--paper);
  }
  .title-thin {
    font-family: "Montserrat", sans-serif;
    font-weight: 200;
    font-size: 86px;
    fill: var(--paper);
  }
  .title-heavy {
    font-family: "Montserrat", sans-serif;
    font-weight: 900;
    font-size: 114px;
    fill: var(--paper);
  }
  .bar { fill: var(--paper); }
</style>
</head>
<body>
  <main class="cover">
    <div class="cover-photo" role="img" aria-label="Close-up photograph of two hands holding a game controller in the dark, its light bar glowing red"></div>

    <svg class="cover-type" width="848" height="1200" viewBox="0 0 848 1200">
      <text class="byline" x="430" y="63" text-anchor="middle">by Martin Quorby</text>

      <text class="title-script" x="430" y="158" text-anchor="middle">Nine</text>

      <text class="title-block" x="209" y="312" textLength="442" lengthAdjust="spacingAndGlyphs">DOORS</text>

      <text class="title-script" x="430" y="378" text-anchor="middle">Past the</text>

      <text class="title-thin" x="114" y="460" textLength="629" lengthAdjust="spacingAndGlyphs">GLOWING</text>

      <text class="title-heavy" x="114" y="577" textLength="634" lengthAdjust="spacingAndGlyphs">SCREEN</text>

      <g class="bars">
        <rect class="bar" x="180" y="570" width="20" height="630"/>
        <rect class="bar" x="282" y="570" width="21" height="630"/>
        <rect class="bar" x="421" y="570" width="21" height="630"/>
        <rect class="bar" x="563" y="570" width="21" height="630"/>
        <rect class="bar" x="658" y="570" width="21" height="630"/>
      </g>
    </svg>
  </main>
</body>
</html>
```